Exciting business card design for diesel performance and offroad business!!

We need a business card design that looks good and stands out. I don't want a plain old boring business card that you forget about and throw away at the end of the day. We are a diesel performance and truck accessory business that sell and install the industries biggest brands and best parts out there!

Industry/Entity Type

Business

Contact Information for Business Card

Dalton Prewick (Owner) 260-587-3146
bramble.motorworks@postmoor.com
Truck and Off-Road Performance and Accessories

Requirements
Must have
• A great look and feel about it. My logo needs to be in center of the card just like the attached picture. On the back I want it to have a list of items we offer
• Truck and Rovex: Lift and Leveling Kits, Intake and Exhaust Systems, Custom Tuning, Wheels and Tires, Steps, Bed Covers, Floor Liners, Custom Lighting, Turbos and Piping, Gauges, Much More!
• UTV: Suspension, Roll Cage, Doors, Exhaust, Tuning, Turbo Kits, Stereo, Wheels/Tires, Custom Lighting, Clutching, Much More!!

```html
<!DOCTYPE html>
<html lang="en">
<head>
<meta charset="utf-8">
<title>Bramble Motorworks – Business Card</title>
<link href="https://fonts.googleapis.com/css2?family=Nanum+Gothic:wght@400;700&display=swap" rel="stylesheet">
<style>
  :root {
    --canvas: #ffffff;
    --ink: #2b2b2b;
    --ink-soft: #3a3a3a;
    --card-edge: #1e1e1e;
    --asphalt-dark: #111010;
    --asphalt-mid: #3a3733;
    --asphalt-light: #5a5650;
    --steel: #d9d9d9;
    --gold-deep: #d98a00;
    --gold: #f5b000;
    --gold-light: #ffe27a;
  }
  * { box-sizing: border-box; margin: 0; padding: 0; }
  html, body {
    width: 1200px; height: 1200px; overflow: hidden;
    background: var(--canvas);
    font-family: "Nanum Gothic", sans-serif;
    color: var(--ink);
  }
  .card {
    position: absolute; left: 174px; width: 852px; height: 474px;
    border: 1px solid var(--card-edge); overflow: hidden; background: #fff;
  }
  .card--front { top: 66px; }
  .card--back { top: 658px; }

  .asphalt {
    position: absolute;
    background: radial-gradient(ellipse at 55% 40%, var(--asphalt-light) 0%, var(--asphalt-mid) 40%, var(--asphalt-dark) 100%);
  }
  .card--front .asphalt { left: 0; top: 0; width: 100%; height: 434px; }

  .brand {
    position: absolute; left: 0; right: 0; top: 0; height: 434px;
    display: flex; align-items: center; justify-content: center; gap: 18px;
  }
  .brand__dot { width: 34px; height: 34px; border-radius: 50%; background: var(--steel); }
  .brand__name {
    font-size: 44px; font-weight: 700; color: var(--steel); letter-spacing: 1px;
  }

  .gold-band {
    position: absolute;
    background: linear-gradient(100deg, var(--gold-deep) 0%, var(--gold) 20%, var(--gold-light) 38%, var(--gold) 55%, var(--gold-deep) 75%, var(--gold) 100%);
  }
  .card--front .gold-band {
    left: 0; bottom: 0; width: 100%; height: 40px;
    display: flex; align-items: center; justify-content: center;
  }
  .front-email { font-size: 28px; color: var(--ink-soft); }

  .card--back .asphalt { left: 0; top: 0; width: 162px; height: 100%; }
  .card--back .gold-band {
    left: 162px; top: 0; width: 82px; height: 100%;
    background: linear-gradient(90deg, var(--gold-light) 0%, var(--gold) 35%, var(--gold-light) 60%, var(--gold-deep) 100%);
  }

  .offer {
    position: absolute; right: 16px; top: 22px; width: 590px;
    text-align: right; color: var(--ink-soft);
  }
  .offer__tagline { font-size: 27px; line-height: 27px; color: var(--ink); margin-bottom: 45px; }
  .offer__group {
    font-size: 26px; line-height: 26.7px; letter-spacing: 0.8px; margin-bottom: 27px;
  }
  .offer__label { color: var(--ink); letter-spacing: 0; }
  .contact-line {
    display: flex; align-items: center; justify-content: flex-end; gap: 10px;
    font-size: 26px; letter-spacing: 0.5px; margin-top: -6px;
  }
  .contact-line__icon { width: 46px; height: 46px; }
  .owner-line { font-size: 27px; color: var(--ink); margin-top: 16px; margin-right: -4px; }
</style>
</head>
<body>

<section class="card card--front">
  <div class="asphalt" role="img" aria-label="Dark textured asphalt background"></div>
  <div class="brand">
    <span class="brand__dot"></span>
    <span class="brand__name">Bramble Motorworks LLC</span>
  </div>
  <div class="gold-band">
    <span class="front-email">bramble.motorworks@postmoor.com</span>
  </div>
</section>

<section class="card card--back">
  <div class="asphalt" role="img" aria-label="Dark textured asphalt background"></div>
  <div class="gold-band" role="img" aria-label="Flowing gold silk band"></div>

  <div class="offer">
    <p class="offer__tagline">Truck and offroad performance<br>and Accessories</p>
    <p class="offer__group"><span class="offer__label">Truck and Rovex:</span> Lift and leveling kits, intake<br>and exhaust systems, custom tuning, wheels<br>and tires, steps, bed covers, floor liners,<br>custom lighting, turbos;</p>
    <p class="offer__group"><span class="offer__label">UTV:</span> Suspension, Roll Cage, doors, exhaust,<br>tuning, turbo kits, stereo, wheels/tires, custom<br>lighting, clutching.</p>
    <p class="contact-line">
      <svg class="contact-line__icon" viewBox="0 0 46 46" aria-hidden="true">
        <circle cx="23" cy="23" r="23" fill="#2b2b2b"/>
        <rect x="11" y="14" width="24" height="18" rx="2" fill="none" stroke="#fff" stroke-width="2.5"/>
        <path d="M11 15 L23 25 L35 15 M11 31 L20 23 M35 31 L26 23" fill="none" stroke="#fff" stroke-width="2.5"/>
      </svg>
      <span>bramble.motorworks@postmoor.com</span>
    </p>
    <p class="owner-line">Dalton Prewick (Owner) 260-587-3146</p>
  </div>
</section>

</body>
</html>
```